Boat and Caravan indoor/ outdoor storage

A new company that provides 4star indoor and outdoor storage for Boats and Caravans
Industry/Entity Type
It Company

```html
<!DOCTYPE html>
<html lang="en">
<head>
<meta charset="utf-8">
<title>Boat and Caravan Storage Flyer</title>
<link rel="stylesheet" href="https://fonts.googleapis.com/css2?family=Arimo:wght@400&display=swap">
<style>
  :root {
    --page: #ffffff;
    --frame-line: #d9cfd6;
    --heading: #3b2463;
    --body-text: #ffffff;
    --tone-orange: #ee5a2f;
    --tone-red: #d6403a;
    --tone-rose: #c8465a;
    --tone-purple: #7b3b8f;
    --tone-violet: #5c3a8c;
  }
  * { margin: 0; padding: 0; box-sizing: border-box; }
  html, body {
    width: 851px;
    height: 1200px;
    overflow: hidden;
    background: var(--page);
  }
  .flyer {
    position: relative;
    width: 851px;
    height: 1200px;
    background: var(--page);
    font-family: "Arimo", Arial, sans-serif;
  }
  .flyer__backdrop {
    position: absolute;
    left: 68px;
    top: 51px;
    width: 715px;
    height: 1084px;
    border: 1px solid var(--frame-line);
    background:
      radial-gradient(ellipse 60% 30% at 30% 20%, rgba(238, 110, 60, 0.9), transparent 70%),
      radial-gradient(ellipse 50% 40% at 80% 55%, rgba(214, 64, 58, 0.85), transparent 70%),
      radial-gradient(ellipse 55% 35% at 15% 75%, rgba(123, 59, 143, 0.9), transparent 70%),
      radial-gradient(ellipse 60% 25% at 60% 95%, rgba(92, 58, 140, 0.95), transparent 75%),
      linear-gradient(175deg, var(--tone-orange) 0%, var(--tone-red) 40%, var(--tone-rose) 65%, var(--tone-purple) 100%);
  }
  .flyer__content {
    position: absolute;
    left: 68px;
    top: 51px;
    width: 715px;
    height: 1084px;
    text-align: center;
  }
  .company-name {
    position: absolute;
    left: 0;
    right: 0;
    top: 66px;
    font-size: 68px;
    line-height: 66px;
    font-weight: 400;
    color: var(--heading);
    opacity: 0.85;
  }
  .info-block {
    position: absolute;
    left: 0;
    right: 0;
    font-size: 30px;
    line-height: 41px;
    color: var(--body-text);
  }
  .info-block--first { top: 280px; }
  .info-block--second { top: 528px; }
  .info-block--third { top: 740px; }
  .tagline {
    position: absolute;
    left: 0;
    right: 0;
    top: 952px;
    font-size: 38px;
    line-height: 58px;
    color: var(--body-text);
  }
</style>
</head>
<body>
  <main class="flyer">
    <div class="flyer__backdrop" role="img" aria-label="Posterised photograph of a boat in storage, in orange, red and purple tones"></div>
    <section class="flyer__content">
      <h1 class="company-name">Company Name<br>Goes Here</h1>
      <p class="info-block info-block--first">
        Text text text texttext text text<br>
        text text text text text text<br>
        text text text texttext text text text<br>
        text text text text text text text text<br>
        text text text text text
      </p>
      <p class="info-block info-block--second">
        Text text text text text text<br>
        text text texttext text text text text<br>
        text text text text text text text text<br>
        text text text text text
      </p>
      <p class="info-block info-block--third">
        Text text text text text text<br>
        text text text texttext text text text<br>
        text text text text text text text text<br>
        text text text text text
      </p>
      <p class="tagline">4 Star Indoor and Outdoor Storage<br>for Boats and Caravans</p>
    </section>
  </main>
</body>
</html>
```